Brightwell-Joinery - DL Flyer - Kitchen Renovations & Cabinetry - Eye Catching Design

Please design a creative, professional DL flyer for us (DL Size: 98 x 210mmm), incorporating details outlined below...

Font: Helvetica Neue (same as logo)

Front: Main logo (01.eps) as a feature, website on the bottom (brightwell-joinery.com.au).

Back: Three key words to be featured: Kitchens I Benchtops I Custom Cabinetry
2-3 clear images showing our work (more have been provided so you can select the images that work the best with the design). We have also attached the icon from our logo on 4 x different colour backgrounds, which could be incorporated (on back).
Text to include: 'Servicing all areas, we come to you!'

Contact details: 'Call us now on 0461 872 309'. enquiries@brightwell-joinery.com.au Lic. No. BLD 738402

Look forward to seeing what you come up with.

Target Market(s)

Home owners, 35-80+ age bracket

Industry/Entity Type

Kitchen

Font styles to use
Other font styles liked:
• Helvetica Neue

Requirements
Must have
• Logo and website on front page of flyer. Minimum of 2-3 images incorporated. Contact details as per project description. Text on back page, 3 key words: Kitchens I Benchtops I Custom Cabinetry
• Creative, eye-catching design layout. Consistent theming with business card (see attached), including colours (grey, white, blues)
Nice to have
• Creative, eye-catching way to incorporate photos.
Should not have
• Not too busy/cluttered

```html
<!DOCTYPE html>
<html lang="en">
<head>
<meta charset="utf-8">
<title>Brightwell-Joinery DL Flyer</title>
<link rel="stylesheet" href="https://fonts.googleapis.com/css2?family=Arimo:wght@400;700&display=swap">
<style>
  :root {
    --backdrop: #a7a7a7;
    --paper: #ffffff;
    --ink: #3f4042;
    --ink-soft: #6b6c6e;
    --brand-blue: #3b88cc;
    --band-grey: #76787b;
    --photo-bath-a: #e9e7e3;
    --photo-bath-b: #cfcbc5;
    --photo-kitchen-a: #efe8dc;
    --photo-kitchen-b: #c9b08a;
    --photo-cabinet-a: #ece7df;
    --photo-cabinet-b: #d8d0c4;
    --photo-office-a: #e8e2d8;
    --photo-office-b: #9e9a8f;
    --photo-shelf-a: #2a1a16;
    --photo-shelf-b: #4a2620;
    --photo-bench-a: #151515;
    --photo-bench-b: #d9d3c7;
  }
  html, body {
    margin: 0;
    padding: 0;
    width: 1200px;
    height: 1200px;
    overflow: hidden;
    background: var(--backdrop);
    font-family: "Arimo", "Helvetica Neue", Arial, sans-serif;
  }
  .flyer-side {
    position: absolute;
    left: 105px;
    width: 992px;
    height: 463px;
    background: var(--paper);
    box-shadow: 4px 6px 10px rgba(0,0,0,0.28);
  }
  .flyer-front { top: 102px; }
  .flyer-back { top: 650px; }
  .flyer-side svg { display: block; width: 992px; height: 463px; }
  .brand-name { font-weight: 700; fill: var(--ink); }
  .tagline { font-size: 17px; fill: var(--ink-soft); letter-spacing: 6px; }
  .web-link { font-size: 26px; fill: var(--brand-blue); }
  .headline { font-size: 33px; fill: var(--paper); }
  .services { font-size: 26px; fill: var(--brand-blue); }
  .call-lead { font-size: 30px; fill: var(--ink); }
  .phone { font-size: 46px; font-weight: 700; fill: #1f1f20; }
  .email { font-size: 21px; fill: #2b2b2c; }
  .licence { font-size: 19px; fill: #2b2b2c; }
</style>
</head>
<body>

<section class="flyer-side flyer-front">
  <svg viewBox="0 0 1240 578" xmlns="http://www.w3.org/2000/svg">
    <defs>
      <linearGradient id="g-bath" x1="0" y1="0" x2="1" y2="1">
        <stop offset="0" stop-color="var(--photo-bath-b)"/><stop offset="1" stop-color="var(--photo-bath-a)"/>
      </linearGradient>
      <linearGradient id="g-kitchen" x1="0" y1="0" x2="1" y2="1">
        <stop offset="0" stop-color="var(--photo-kitchen-a)"/><stop offset="1" stop-color="var(--photo-kitchen-b)"/>
      </linearGradient>
      <linearGradient id="g-cabinet" x1="0" y1="0" x2="0" y2="1">
        <stop offset="0" stop-color="var(--photo-cabinet-a)"/><stop offset="1" stop-color="var(--photo-cabinet-b)"/>
      </linearGradient>
      <linearGradient id="g-office" x1="0" y1="0" x2="0" y2="1">
        <stop offset="0" stop-color="var(--photo-office-a)"/><stop offset="1" stop-color="var(--photo-office-b)"/>
      </linearGradient>
    </defs>

    <polygon class="photo-bathroom" role="img" aria-label="Photo of a white bathroom vanity with basin and teal towels"
      points="210,0 744,0 744,32 391,217 210,127" fill="url(#g-bath)"/>
    <polygon class="photo-handle" role="img" aria-label="Photo detail of a cabinet door handle"
      points="891,90 935,57 977,80 977,164 933,145 891,118" fill="var(--photo-cabinet-a)"/>
    <polygon class="photo-cabinet" role="img" aria-label="Photo of built-in cream cabinets with display niche"
      points="1012,0 1240,0 1240,212 1062,212 1012,185" fill="url(#g-cabinet)"/>
    <polygon class="photo-office" role="img" aria-label="Photo of a built-in home office desk with shelving"
      points="1058,245 1240,242 1240,578 1003,578 1003,303 1058,303" fill="url(#g-office)"/>
    <polygon class="photo-kitchen" role="img" aria-label="Photo of a white shaker-style kitchen with oven and rangehood"
      points="550,198 745,97 938,198 938,578 550,578" fill="url(#g-kitchen)"/>

    <polyline class="divider-chevron" points="530,355 746,272 960,372" fill="none" stroke="var(--paper)" stroke-width="24"/>
    <rect class="logo-band" x="550" y="343" width="390" height="96" fill="var(--paper)" opacity="0.6"/>

    <text class="brand-name" x="33" y="394" font-size="50" textLength="608" lengthAdjust="spacingAndGlyphs">BRIGHTWELL-JOINERY</text>
    <text class="tagline" x="37" y="428" textLength="604" lengthAdjust="spacing">CABINETRY SOLUTIONS FOR YOUR HOME</text>
    <text class="web-link" x="37" y="538">brightwell-joinery.com.au</text>
  </svg>
</section>

<section class="flyer-side flyer-back">
  <svg viewBox="0 0 1240 578" xmlns="http://www.w3.org/2000/svg">
    <defs>
      <linearGradient id="g-sink" x1="0" y1="0" x2="1" y2="1">
        <stop offset="0" stop-color="#e6e4df"/><stop offset="1" stop-color="#cfd8d2"/>
      </linearGradient>
      <linearGradient id="g-shelf" x1="0" y1="0" x2="1" y2="0">
        <stop offset="0" stop-color="var(--photo-shelf-b)"/><stop offset="1" stop-color="var(--photo-shelf-a)"/>
      </linearGradient>
      <linearGradient id="g-bench" x1="0" y1="0" x2="0" y2="1">
        <stop offset="0" stop-color="var(--photo-bench-a)"/><stop offset="0.45" stop-color="#3a3835"/><stop offset="1" stop-color="var(--photo-bench-b)"/>
      </linearGradient>
    </defs>

    <polygon class="photo-sink" role="img" aria-label="Photo of a kitchen with marble benchtop, sink and glass splashback"
      points="464,0 834,0 834,330 464,422" fill="url(#g-sink)"/>
    <polygon class="photo-shelving" role="img" aria-label="Photo of floor-to-ceiling dark timber shelving with library ladder"
      points="870,0 1240,0 1240,258 870,323" fill="url(#g-shelf)"/>
    <polygon class="photo-benchtop" role="img" aria-label="Photo of a long black stone benchtop over cream drawers"
      points="464,438 1179,278 1240,293 1240,578 464,578" fill="url(#g-bench)"/>

    <rect class="headline-band" x="0" y="40" width="804" height="80" fill="var(--band-grey)" opacity="0.95"/>
    <rect class="services-band" x="0" y="120" width="655" height="60" fill="var(--paper)" opacity="0.7"/>

    <text class="headline" x="28" y="93">SERVICING ALL AREAS, WE COME TO YOU!</text>
    <text class="services" x="28" y="162">KITCHENS | BENCHTOPS | CUSTOM CABINETRY</text>

    <text class="call-lead" x="28" y="338">Call us now on</text>
    <text class="phone" x="28" y="402">0461 872 309</text>

    <g class="email-icon">
      <circle cx="44" cy="444" r="16" fill="var(--ink-soft)"/>
      <rect x="35" y="438" width="18" height="12" fill="none" stroke="var(--paper)" stroke-width="1.8"/>
      <polyline points="35,438 44,445 53,438" fill="none" stroke="var(--paper)" stroke-width="1.8"/>
    </g>
    <text class="email" x="66" y="451">enquiries@brightwell-joinery.com.au</text>
    <text class="licence" x="28" y="498">LIC. NO. BLD 738402</text>
  </svg>
</section>

</body>
</html>
```